11th Annual VarTQ Forum Flyer - Save the Date

We need a flyer for our annual Forum that will be creative with the theme of the Forum while highlighting our conference Title and Topics. Flyer should allow for a header that can be used consistently across conference communication. This is our 11th Annual Forum, which will take place outside of Houston, Texas at El Mirador Resort and Spa.

Target Market(s)

Architects, engineers, contractors, universities, building project Owners

Industry/Entity Type

Construction

Font styles to use
Sans Serif

Colors

Designer to choose colors to be used in the design.

Requirements
Must have
• Title, date, location, key topics (title only), logo. See attached for breakdown of information.
Nice to have
• Creativity with the theme of the Forum, ability to slice flyer so that a portion can be used for a header in other conference documents.
• Mention of Closing Keynote, Dale Porter
Should not have
• Please don't use the topic descriptions in the Flyer. Just the main titles of the topics is necessary.
• Should not be too word, but eye-catching with graphics and main

```html
<!DOCTYPE html>
<html lang="en">
<head>
<meta charset="utf-8">
<title>11th VarTQ Annual Forum – Save the Date</title>
<link rel="stylesheet" href="https://fonts.googleapis.com/css2?family=Montserrat:wght@500;600;700&family=Open+Sans:wght@700;800&family=PT+Sans+Narrow:wght@400;700&display=swap">
<style>
  :root {
    --navy: #1b2a6b;
    --navy-deep: #141f55;
    --navy-glow: #2f79c8;
    --green: #8cbb42;
    --ink: #1f1f1f;
    --row-dark: #232323;
    --divider: #d6d6d6;
    --white: #ffffff;
    --logo-grey: #5a5a5a;
  }
  * { margin: 0; padding: 0; box-sizing: border-box; }
  html, body { width: 927px; height: 1200px; overflow: hidden; background: var(--white); }
  .flyer { position: relative; width: 927px; height: 1200px; overflow: hidden; font-family: "Montserrat", sans-serif; background: var(--divider); }

  .hero-photo { position: absolute; left: 0; top: 0; width: 927px; height: 480px;
    background: linear-gradient(160deg, #7fa6d8 0%, #b9d2ee 30%, #5d87c2 55%, #2e5c9c 80%, #1d3f78 100%); }

  .logo-tab { position: absolute; left: 85px; top: 0; width: 290px; height: 126px; background: var(--white);
    box-shadow: 0 4px 10px rgba(0,0,0,.25); display: flex; align-items: center; justify-content: center; gap: 14px; }
  .logo-square { width: 22px; height: 22px; background: var(--green); }
  .logo-name { color: var(--logo-grey); font-family: "Montserrat", sans-serif; font-weight: 600; font-size: 38px; letter-spacing: 1px; }

  .save-date { position: absolute; left: 340px; top: 150px; color: var(--white); font-family: "Montserrat", sans-serif;
    font-weight: 700; font-size: 58px; line-height: 60px; letter-spacing: 2px; }

  .theme-bar { position: absolute; left: 0; top: 372px; width: 927px; height: 98px; background: var(--green);
    display: flex; flex-direction: column; justify-content: center; padding-left: 335px;
    font-family: "Open Sans", sans-serif; font-weight: 800; color: var(--ink); font-size: 27px; line-height: 36px; letter-spacing: 1px; }
  .topics-label { position: absolute; left: 0; top: 470px; width: 927px; height: 56px; background: var(--divider);
    padding-left: 445px; line-height: 56px; font-weight: 600; font-size: 17px; color: var(--ink); }

  .topic { position: absolute; left: 0; width: 927px; background: var(--row-dark); }
  .topic-title { position: absolute; left: 445px; color: var(--white); font-weight: 700; font-size: 21px; line-height: 28px; }
  .topic-photo { position: absolute; right: 0; top: 0; width: 260px; height: 100%;
    clip-path: polygon(0 0, 100% 0, 100% 100%, 12% 100%); }
  .photo-contract { background: linear-gradient(135deg, #e9eef3, #b9c3cc 60%, #dfe4ea); }
  .photo-culture { background: linear-gradient(135deg, #5b4a38, #8b7a62 50%, #3e4652); }
  .photo-site { background: linear-gradient(180deg, #4d6a9c, #d48a4a 60%, #f2b45a 75%, #2a2a2a); }

  .keynote { position: absolute; left: 0; top: 985px; width: 927px; height: 110px; background: var(--row-dark); color: var(--white); text-align: center; padding-left: 490px; }
  .keynote-label { font-weight: 500; font-size: 16px; margin-top: 26px; }
  .keynote-name { font-weight: 700; font-size: 28px; margin-top: 4px; letter-spacing: 1px; }

  .contact { position: absolute; left: 0; top: 1095px; width: 927px; height: 105px; background: var(--green); padding-left: 490px; text-align: center; color: var(--ink); }
  .contact-label { font-size: 20.5px; font-weight: 500; margin-top: 18px; letter-spacing: 1px; }
  .contact-phone { display: inline-flex; align-items: center; gap: 12px; font-weight: 700; font-size: 25px; margin-top: 4px; letter-spacing: 1px; }

  .side-panel { position: absolute; left: 0; top: 0; width: 927px; height: 1200px; pointer-events: none; }
  .edition { position: absolute; left: 62px; top: 418px; width: 146px; height: 146px; border-radius: 50%; background: var(--green);
    color: var(--white); font-weight: 700; font-size: 50px; display: flex; align-items: center; justify-content: center; }
  .edition sup { font-size: 28px; margin-top: -22px; }
  .forum-name { position: absolute; left: 0; top: 578px; width: 270px; text-align: center; font-weight: 700; font-size: 44px; line-height: 52px; color: var(--white); }
  .forum-name .brand { color: var(--green); }
  .when { position: absolute; left: 42px; top: 826px; font-family: "PT Sans Narrow", sans-serif; font-weight: 700; color: var(--green); font-size: 41.5px; line-height: 52px; }
  .venue { position: absolute; left: 42px; top: 992px; color: var(--white); font-family: "PT Sans Narrow", sans-serif; font-style: normal; }
  .venue-name { font-weight: 700; font-size: 43px; line-height: 54px; }
  .venue-address { font-size: 23px; line-height: 33px; margin-top: 4px; }
</style>
</head>
<body>
<main class="flyer">
  <div class="hero-photo" role="img" aria-label="Glass office towers against a blue sky with a businessman seated on a wooden stool"></div>

  <div class="logo-tab">
    <span class="logo-square"></span><span class="logo-name">VarTQ</span>
  </div>

  <h1 class="save-date">SAVE<br>THE<br>DATE</h1>

  <div class="theme-bar"><span>The Three-legged Stool</span><span>&nbsp;– Balanced or Broken?</span></div>
  <div class="topics-label">Three Key Topics:</div>

  <section class="topic" style="top:527px;height:143px">
    <p class="topic-title" style="top:30px">The Right<br>Contract<br>Management</p>
    <div class="topic-photo photo-contract" role="img" aria-label="Business handshake over a contract document"></div>
  </section>
  <section class="topic" style="top:681px;height:143px">
    <p class="topic-title" style="top:42px">The Right<br>Culture</p>
    <div class="topic-photo photo-culture" role="img" aria-label="Team gathered around a table in an open office"></div>
  </section>
  <section class="topic" style="top:835px;height:143px">
    <p class="topic-title" style="top:42px">The Right<br>Subcontractors</p>
    <div class="topic-photo photo-site" role="img" aria-label="Construction workers on steel framing at sunset"></div>
  </section>

  <section class="keynote">
    <p class="keynote-label">Closing Keynote</p>
    <p class="keynote-name">Dale Porter</p>
  </section>

  <section class="contact">
    <p class="contact-label">For more information:</p>
    <p class="contact-phone">
      <svg width="22" height="22" viewBox="0 0 24 24" aria-hidden="true"><circle cx="12" cy="12" r="11" fill="none" stroke="#1f1f1f" stroke-width="1.5"/><path d="M8 6.5c.6-.5 1.3-.4 1.6.2l1 2c.2.5 0 1-.4 1.3l-.8.6c.5 1.4 1.5 2.6 2.9 3.4l.7-.7c.4-.4.9-.5 1.3-.2l1.9 1.2c.5.3.6 1 .2 1.5l-.8.9c-.8.8-2.3.7-4.2-.5-2.300-1.500-4-3.800-4.300-6.100-.2-1.2.1-2.1.9-2.6z" fill="#1f1f1f"/></svg>
      +1 555-014-2290
    </p>
  </section>

  <svg class="side-panel" viewBox="0 0 927 1200" aria-hidden="true">
    <defs>
      <radialGradient id="panelGlow" cx="0.22" cy="0.3" r="0.6">
        <stop offset="0" stop-color="#2f79c8"/>
        <stop offset="0.55" stop-color="#1b2a6b"/>
        <stop offset="1" stop-color="#141f55"/>
      </radialGradient>
    </defs>
    <polygon points="0,170 276,170 490,1200 0,1200" fill="url(#panelGlow)"/>
  </svg>

  <div class="edition">11<sup>th</sup></div>
  <h2 class="forum-name"><span class="brand">VarTQ</span><br>Annual<br>Forum</h2>
  <p class="when">September 9 &amp;10<br>8:00 AM to 4:00 PM</p>
  <address class="venue">
    <div class="venue-name">El Mirador<br>Lake Resort &amp; Spa</div>
    <div class="venue-address">410 Mirador Blvd<br>Lakeview, Texas 77390</div>
  </address>
</main>
</body>
</html>
```